Memoir author looking for book cover design

Title:
"Tides, Thorns and Twilight"

Subtitle:
"The Journey to Reach my Brother, Vanished on the Glacier"

My book is about the 18-month-long search and grieving process after my husband went missing from a hiking accident.
See "notesbeyondthequietfjord.example" for background

(An "ampersand" may look best, but I'm unable to enter it in this format)

Reason: Having difficulty finishing up, in part due to time difference. Don't want designers to have to work in the middle of the night!

```html
<!DOCTYPE html>
<html lang="en">
<head>
<meta charset="utf-8">
<title>Tides, Thorns and Twilight — Book Cover</title>
<link rel="stylesheet" href="https://fonts.googleapis.com/css2?family=Anton&family=Josefin+Sans:wght@400&display=swap">
<style>
  :root {
    --paper: #ffffff;
    --paper-edge: #e9e9e9;
    --ink: #141414;
    --sky-deep: #3d78b5;
    --sky-pale: #b9cfe3;
    --ridge: #6e7f72;
    --slope: #6f8a3a;
    --rock: #8c8a74;
  }
  html, body {
    margin: 0;
    padding: 0;
    overflow: hidden;
    background: var(--paper);
  }
  .cover {
    position: relative;
    width: 821px;
    height: 1200px;
    overflow: hidden;
    background: radial-gradient(ellipse at 50% 50%, var(--paper) 55%, var(--paper-edge) 100%);
  }
  .title-art {
    position: absolute;
    left: 0;
    top: 0;
    width: 821px;
    height: 860px;
  }
  .title-line {
    font-family: "Anton", "Impact", sans-serif;
    text-transform: uppercase;
  }
  .subtitle {
    position: absolute;
    left: 0;
    right: 0;
    top: 884px;
    margin: 0;
    text-align: center;
    font-family: "Josefin Sans", "Helvetica Neue", sans-serif;
    font-weight: 400;
    font-size: 31px;
    line-height: 45px;
    letter-spacing: 0.5px;
    color: var(--ink);
    text-transform: uppercase;
  }
  .author {
    position: absolute;
    left: 0;
    right: 0;
    top: 1092px;
    margin: 0;
    text-align: center;
    font-family: "Josefin Sans", "Helvetica Neue", sans-serif;
    font-weight: 400;
    font-size: 66px;
    line-height: 1;
    letter-spacing: 17px;
    padding-left: 17px;
    color: var(--ink);
    text-transform: uppercase;
  }
</style>
</head>
<body>
  <main class="cover">
    <svg class="title-art" viewBox="0 0 821 860" role="img"
         aria-label="Title lettering filled with a photograph of a hiker in a cap and checked shirt standing on a mountain ridge under a blue sky">
      <defs>
        <linearGradient id="landscape-fill" gradientUnits="userSpaceOnUse" x1="0" y1="96" x2="0" y2="842">
          <stop offset="0" stop-color="var(--sky-deep)"/>
          <stop offset="0.32" stop-color="var(--sky-pale)"/>
          <stop offset="0.38" stop-color="var(--ridge)"/>
          <stop offset="0.6" stop-color="var(--slope)"/>
          <stop offset="0.85" stop-color="var(--slope)"/>
          <stop offset="1" stop-color="var(--rock)"/>
        </linearGradient>
      </defs>
      <g fill="url(#landscape-fill)">
        <text class="title-line" x="86" y="374" font-size="321" textLength="638" lengthAdjust="spacingAndGlyphs">Tides</text>
        <text class="title-line" x="86" y="660" font-size="317" textLength="640" lengthAdjust="spacingAndGlyphs">Thorns</text>
        <text class="title-line" x="84" y="842" font-size="192" textLength="656" lengthAdjust="spacingAndGlyphs">&amp; Twilight</text>
      </g>
    </svg>

    <p class="subtitle">The Journey to Reach my Brother,<br>Vanished on the Glacier</p>

    <p class="author">Author Name</p>
  </main>
</body>
</html>
```